Plumbing Business needs a more appealing business card design and logo

card must include phone number and logo, open to new logo ideas, full creative freedom

Industry/Entity Type

Plumbing

Contact Information for Business Card

Derek Halloway
0417385521

Logo Text

call outs from $80

Font styles to use
Other font styles liked:
• unsure

Colors
ec1f27
0255a3
f78f20

```html
<!DOCTYPE html>
<html lang="en">
<head>
<meta charset="utf-8">
<title>Brightwater Plumbing – Business Card</title>
<link rel="stylesheet" href="https://fonts.googleapis.com/css2?family=Lato:wght@400;700;900&display=swap">
<style>
  :root {
    --page-bg: #ffffff;
    --card-white: #fbfbfb;
    --brand-blue: #0561b8;
    --brand-blue-light: #0a72c4;
    --brand-blue-dark: #0255a3;
    --ink: #2a2a2a;
    --muted: #4a4a4a;
    --line-grey: #e3e3e3;
  }
  * { box-sizing: border-box; margin: 0; padding: 0; }
  html, body {
    width: 1200px; height: 1200px; overflow: hidden;
    background: var(--page-bg);
    font-family: "Lato", Arial, sans-serif;
  }
  .canvas {
    width: 1200px; height: 1200px;
    display: flex; flex-direction: column; align-items: center; justify-content: center;
    gap: 60px;
  }
  .card {
    position: relative;
    width: 840px; height: 480px;
    border-radius: 22px;
    overflow: hidden;
    box-shadow: 0 10px 30px rgba(0,0,0,0.14);
  }

  /* Front */
  .card-front { background: var(--card-white); }
  .card-front .bottom-band {
    position: absolute; left: 0; right: 0; bottom: 0; height: 22px;
    background: var(--brand-blue);
  }
  .brand {
    position: absolute; left: 60px; top: 64px;
    display: flex; align-items: center; gap: 18px;
  }
  .brand-dot {
    width: 58px; height: 58px; border-radius: 50%;
    background: var(--brand-blue);
  }
  .brand-name {
    font-weight: 900; font-size: 30px; letter-spacing: 1px;
    text-transform: uppercase; color: var(--brand-blue);
    line-height: 1;
  }
  .person { position: absolute; left: 60px; top: 250px; }
  .person-name {
    font-weight: 700; font-size: 42px; letter-spacing: 0.5px;
    text-transform: uppercase; color: var(--brand-blue-dark);
  }
  .person-role { font-size: 20px; color: var(--muted); margin-top: 6px; }
  .contact-list { position: absolute; left: 60px; top: 360px; list-style: none; }
  .contact-item {
    display: flex; align-items: center; gap: 16px;
    font-size: 26px; color: var(--ink); letter-spacing: 0.5px;
    height: 40px;
  }
  .contact-item svg { width: 24px; height: 24px; fill: var(--ink); flex: none; }

  /* Back */
  .card-back {
    background: linear-gradient(160deg, var(--brand-blue-light) 0%, var(--brand-blue) 55%, var(--brand-blue-dark) 100%);
    display: flex; align-items: center; justify-content: center; gap: 20px;
  }
  .card-back .brand-dot { background: #ffffff; width: 44px; height: 44px; }
  .card-back .brand-name { color: #ffffff; font-size: 44px; letter-spacing: 2px; }
</style>
</head>
<body>
<main class="canvas">

  <section class="card card-front" aria-label="Business card front">
    <div class="brand">
      <span class="brand-dot"></span>
      <span class="brand-name">Brightwater Plumbing</span>
    </div>

    <div class="person">
      <h1 class="person-name">Derek Halloway</h1>
      <p class="person-role">Position</p>
    </div>

    <ul class="contact-list">
      <li class="contact-item">
        <svg viewBox="0 0 24 24" aria-hidden="true"><path d="M6.6 10.8a15.1 15.1 0 0 0 6.6 6.6l2.2-2.2c.3-.3.7-.4 1-.2 1.1.4 2.3.6 3.6.6.6 0 1 .4 1 1V20c0 .6-.4 1-1 1A17 17 0 0 1 3 4c0-.6.4-1 1-1h3.5c.6 0 1 .4 1 1 0 1.3.2 2.5.6 3.6.1.3 0 .7-.2 1L6.6 10.8z"/></svg>
        <span>0417385521</span>
      </li>
      <li class="contact-item">
        <svg viewBox="0 0 24 24" aria-hidden="true"><path d="M2 5h20v14H2V5zm2 2v.3l8 5.2 8-5.2V7H4zm0 2.7V17h16V9.7l-8 5.2-8-5.2z"/></svg>
        <span>derek.halloway@mailbox.net</span>
      </li>
    </ul>

    <div class="bottom-band"></div>
  </section>

  <section class="card card-back" aria-label="Business card back">
    <span class="brand-dot"></span>
    <span class="brand-name">Brightwater Plumbing</span>
  </section>

</main>
</body>
</html>
```